Consultative Employee Benifits Firm Needs Business Card Design Project

We need a business card design for a new company based in Northern Virginia called "Telman Financial Services, LLC. We are both a wealth management advisory firm, as well as an employee benefits firm, which strives to provide superior creativity in employee benefits plan design and greater client and employee satisfaction. We are obsessed with service and follow up.

Our firm specializes in the areas of group health, life, dental, disability, voluntary benefits, Executive Benefits, HRA and HSA programs. We offer competitive employee benefit packages and pricing models for single or multi-state/multi location companies by maintaining preferred relationships with a large number of regional and national carriers.

Our firm also considers the many dimensions of your wealth through an integrated process we call wealth structuring — a comprehensive, dynamic approach to building, preserving, enjoying and transferring your wealth. And because we are often dealing with complex ownership structures and complicated, changing family dynamics, we bring the highest level of experience and creativity to managing your wealth. We work hard to help ensure that your legacy lasts by preparing your children for the financial challenges and opportunities that are headed their way.

Our final design should communicate an integrated approach to finanial safety and optimization
Updates

 Due to a few designers not accepting due to low budget, I have increased budget payout 19%. 

Project Deadline Extended
Reason: I have only heard from 12 designers. So, maybe I did not give the right amount of time to do the project. For the designers that have submitted their designs, thank you. I have seen three or four designs that I liked and might end up with one of them after it's all over, but I thought I would see between 20 - 25 before everything was over. Dan

Target Market(s)

Professionals; doctors, contractors, small to mid size business owners, ages 50 -65 with nert worth of 2MM

Industry/Entity Type

Financial

Requirements
Must have
• Telman Financial Services, LLC

Dan Telman
President
41957 Marwick Hollow Street
Quenford Glen, 20871

Office: 703 555-0184
Cell: 703 555-0127
Fax: 703 555-0163
Email: dantelman@quorvex.net
Should not have
• No pink or yellow colors.
No generic clipart (coins, dollar signs, money bags, graphs)

```html
<!DOCTYPE html>
<html lang="en">
<head>
<meta charset="utf-8">
<title>Telman Financial Services, LLC — Business Card</title>
<link rel="stylesheet" href="https://fonts.googleapis.com/css2?family=Cinzel:wght@600;700&family=Tinos&display=swap">
<style>
  :root {
    --page-bg: #ffffff;
    --card-green: #99a47a;
    --card-green-deep: #8c976c;
    --band-light: #e6e3da;
    --band-mid: #c9c5b7;
    --band-edge: #b3ae9e;
    --rule-dark: #6f7556;
    --title-ink: #5b6146;
    --name-ink: #f2f1e8;
    --body-ink: #f6f5ee;
    --shadow-ink: rgba(40, 44, 26, 0.75);
    --divider: #eeeedf;
    --flourish: rgba(255, 255, 255, 0.10);
  }
  * { margin: 0; padding: 0; box-sizing: border-box; }
  html, body {
    width: 1200px;
    height: 900px;
    overflow: hidden;
    background: var(--page-bg);
  }
  .business-card {
    position: absolute;
    left: 94px;
    top: 160px;
    width: 1012px;
    height: 580px;
    background: linear-gradient(160deg, var(--card-green) 0%, var(--card-green-deep) 100%);
    box-shadow: 2px 3px 8px rgba(0, 0, 0, 0.35);
    overflow: hidden;
  }
  .flourish-area {
    position: absolute;
    left: 20px;
    top: 250px;
    width: 900px;
    height: 260px;
    border-radius: 50%;
    background: radial-gradient(ellipse at center, var(--flourish) 0%, rgba(255,255,255,0) 70%);
  }
  .name-band-rule {
    position: absolute;
    left: 0;
    width: 100%;
    height: 4px;
    background: var(--rule-dark);
  }
  .name-band-rule.top { top: 38px; }
  .name-band-rule.bottom { top: 164px; }
  .name-band {
    position: absolute;
    left: 0;
    top: 50px;
    width: 100%;
    height: 106px;
    background: linear-gradient(90deg, var(--band-mid) 0%, var(--band-light) 50%, var(--band-mid) 100%);
    border-top: 2px solid var(--band-edge);
    border-bottom: 2px solid var(--band-edge);
    display: flex;
    align-items: center;
    justify-content: center;
  }
  .company-name {
    font-family: "Cinzel", serif;
    font-weight: 700;
    font-size: 45px;
    letter-spacing: 2px;
    color: var(--title-ink);
    white-space: nowrap;
  }
  .person-title {
    position: absolute;
    left: 62px;
    top: 188px;
    font-family: "Cinzel", serif;
    font-weight: 700;
    font-size: 34px;
    letter-spacing: 3px;
    color: var(--name-ink);
    text-shadow: 2px 2px 2px var(--shadow-ink);
    white-space: nowrap;
  }
  .contact-block {
    position: absolute;
    right: 62px;
    font-family: "Tinos", serif;
    font-size: 36px;
    line-height: 40px;
    color: var(--body-ink);
    text-align: right;
    text-shadow: 2px 2px 2px var(--shadow-ink);
    white-space: nowrap;
  }
  .address { top: 302px; }
  .phones { top: 418px; line-height: 36px; }
  .divider {
    position: absolute;
    left: 60px;
    right: 62px;
    top: 396px;
    height: 2px;
    background: var(--divider);
    box-shadow: 1px 1px 1px rgba(40, 44, 26, 0.4);
  }
</style>
</head>
<body>
  <div class="business-card">
    <div class="flourish-area" role="img" aria-label="Faint decorative flourish swash behind the contact details"></div>

    <div class="name-band-rule top"></div>
    <div class="name-band">
      <h1 class="company-name">Telman Financial Services, LLC</h1>
    </div>
    <div class="name-band-rule bottom"></div>

    <p class="person-title">Dan Telman - President</p>

    <address class="contact-block address" style="font-style:normal">
      41957 Marwick Hollow Street<br>
      Quenford Glen, 20871
    </address>

    <div class="divider"></div>

    <div class="contact-block phones">
      Office: 703 555-0184 • Cell: 703 555-0127<br>
      Fax: 703 555-0163<br>
      Email: dantelman@quorvex.net
    </div>
  </div>
</body>
</html>
```